Business Cards and Stationary for Physio
Brookvale Phsyiotherapy Clinic
Business Cards and Stationary for Physio -
Creative Brief
Simple
First Last
Physiotherapist B. Physio
Street Name, City, Zip
info@brookvalephysiotherapy.example
www.brookvalephysiotherapy.example
Brookvale Phsyiotherapy Clinic. Next Appointment Date Time

```html
<!DOCTYPE html>
<html lang="en">
<head>
<meta charset="utf-8">
<title>Brookvale Phsyiotherapy Clinic – Business Card</title>
<link rel="stylesheet" href="https://fonts.googleapis.com/css2?family=Open+Sans:wght@400;600;700&display=swap">
<style>
  :root {
    --page-bg: #eef0f2;
    --card-white: #ffffff;
    --brand-green: #7cb83a;
    --brand-green-deep: #6aa72e;
    --brand-blue: #27338f;
    --text-white: #ffffff;
    --card-shadow: rgba(20, 30, 60, 0.18);
  }
  * { box-sizing: border-box; margin: 0; padding: 0; }
  html, body {
    width: 1200px;
    height: 929px;
    overflow: hidden;
    background: var(--page-bg);
    font-family: "Open Sans", Arial, sans-serif;
  }
  .stage {
    position: relative;
    width: 1200px;
    height: 929px;
  }
  .business-card {
    position: absolute;
    left: 180px;
    top: 224px;
    width: 840px;
    height: 480px;
    border-radius: 34px;
    overflow: hidden;
    background: var(--card-white);
    box-shadow: 0 18px 40px var(--card-shadow);
  }
  .card-colour-field {
    position: absolute;
    left: 0;
    right: 0;
    top: 176px;
    bottom: 0;
    background: linear-gradient(90deg, var(--brand-green) 0%, var(--brand-green-deep) 100%);
  }

  .clinic-brand {
    position: absolute;
    left: 60px;
    top: 52px;
    display: flex;
    align-items: center;
    gap: 14px;
  }
  .brand-dot {
    width: 30px;
    height: 30px;
    border-radius: 50%;
    background: var(--brand-green);
  }
  .brand-name {
    color: var(--brand-blue);
    font-weight: 700;
    font-size: 24px;
    letter-spacing: 0.5px;
  }

  .practitioner {
    position: absolute;
    left: 48px;
    top: 212px;
    color: var(--text-white);
  }
  .practitioner-name {
    font-weight: 700;
    font-size: 42px;
    line-height: 1;
  }
  .practitioner-title {
    font-weight: 600;
    font-size: 14px;
    margin-top: 4px;
    margin-left: 2px;
  }
  .contact-details {
    position: absolute;
    left: 48px;
    top: 308px;
    list-style: none;
    color: var(--text-white);
    font-size: 19px;
    line-height: 1.3;
  }
</style>
</head>
<body>
  <main class="stage">
    <section class="business-card" aria-label="Brookvale Phsyiotherapy Clinic business card">
      <div class="card-colour-field" role="img" aria-label="Green and blue decorative wave across the lower card"></div>

      <div class="clinic-brand">
        <span class="brand-dot"></span>
        <span class="brand-name">Brookvale Phsyiotherapy Clinic</span>
      </div>

      <div class="practitioner">
        <h1 class="practitioner-name">First Last</h1>
        <p class="practitioner-title">Physiotherapist B. Physio</p>
      </div>

      <ul class="contact-details">
        <li>Street Name, City, Zip</li>
        <li>Phone: 613-555-0142</li>
        <li>Email: info@brookvalephysiotherapy.example</li>
        <li>Web address: www.brookvalephysiotherapy.example</li>
      </ul>
    </section>
  </main>
</body>
</html>
```